Breakfast Briefings / Lunch & Learn

I would like to have a double sided flyer size 8x10 to display the breakfast briefing on one side and Lunch & Learn on the other side.

Header on each side to say
2018 Calendar Breakfast Briefing (on the breakfast side)
2018 Calendar Lunch & Learn (on the lunch side)

I have attached a copy of the files we would like to use.

Learn

```html
<!DOCTYPE html>
<html lang="en">
<head>
<meta charset="UTF-8">
<title>2018 Calendar Lunch &amp; Learn</title>
<link rel="stylesheet" href="https://fonts.googleapis.com/css2?family=Lato:wght@400;700&family=Montserrat:wght@400;900&family=Raleway:wght@200;300;400&display=swap">
<style>
  :root {
    --blue-deep: #021a4d;
    --blue-mid: #0a3f9e;
    --blue-bright: #0a5fc2;
    --paper: #f8f8f8;
    --ink: #333333;
    --rule: #c9c9c9;
    --orange: #f7a02a;
    --white: #ffffff;
    --teal: #1a8fc4;
    --brand-grey: #555b63;
  }
  * { margin: 0; padding: 0; box-sizing: border-box; }
  html, body { width: 848px; height: 1200px; overflow: hidden; }
  body { background: var(--paper); font-family: "Lato", sans-serif; }

  .flyer { position: relative; width: 848px; height: 1200px; background: var(--paper); overflow: hidden; }

  .side-panel {
    position: absolute; left: 0; top: 0; width: 370px; height: 1200px;
    background:
      linear-gradient(160deg, rgba(255,255,255,0) 40%, rgba(80,160,255,0.18) 55%, rgba(255,255,255,0) 70%),
      linear-gradient(200deg, rgba(0,0,0,0) 55%, rgba(0,0,0,0.35) 85%),
      linear-gradient(180deg, var(--blue-mid) 0%, var(--blue-bright) 45%, var(--blue-mid) 70%, var(--blue-deep) 100%);
  }
  .panel-notch { position: absolute; left: 370px; top: 58px; }

  .calendar-badge { position: absolute; left: 63px; top: 167px; }

  .title { position: absolute; left: 63px; top: 268px; color: var(--white); }
  .title-year { font-family: "Raleway", sans-serif; font-weight: 200; font-size: 64px; line-height: 64px; letter-spacing: -1px; }
  .title-kicker { font-family: "Raleway", sans-serif; font-weight: 400; font-size: 31px; line-height: 34px; margin-top: 4px; letter-spacing: 1px; }
  .title-main { font-family: "Montserrat", sans-serif; font-weight: 900; font-size: 70px; line-height: 60px; margin-top: 6px; letter-spacing: -1px; }
  .title-sub { font-family: "Montserrat", sans-serif; font-size: 64px; line-height: 62px; white-space: nowrap; }
  .title-amp { font-family: "Raleway", sans-serif; font-weight: 300; }
  .title-accent { color: var(--orange); font-weight: 900; }
  .title-rule { position: absolute; left: 67px; top: 507px; width: 92px; height: 3px; background: var(--white); }

  .meal-icons { position: absolute; left: 70px; top: 572px; }

  .site-url {
    position: absolute; left: 51px; top: 1121px; padding-left: 13px;
    border-left: 3px solid var(--orange);
    color: var(--white); font-family: "Raleway", sans-serif; font-size: 21px; letter-spacing: 4px; line-height: 26px;
  }

  .brand { position: absolute; left: 446px; top: 72px; display: flex; align-items: center; gap: 10px; }
  .brand-dot { width: 14px; height: 14px; border-radius: 50%; background: var(--teal); }
  .brand-name { font-family: "Lato", sans-serif; font-weight: 400; font-size: 30px; letter-spacing: 5px; color: var(--brand-grey); }

  .schedule { position: absolute; left: 433px; top: 272px; width: 313px; }
  .schedule-row { display: flex; border-top: 1px solid var(--rule); font-size: 19px; line-height: 24px; color: var(--ink); }
  .schedule-row:first-child { border-top: none; }
  .schedule-month { width: 89px; flex: none; border-right: 1px solid var(--rule); padding: 8px 0 0 5px; font-weight: 700; }
  .schedule-topic { padding: 8px 0 0 16px; white-space: nowrap; }
  .schedule-row:first-child .schedule-month,
  .schedule-row:first-child .schedule-topic { padding-top: 2px; }

  .motto {
    position: absolute; left: 428px; top: 1004px;
    font-family: "Raleway", sans-serif; font-weight: 300; font-size: 56px; line-height: 50px;
    color: var(--teal); letter-spacing: -1px;
  }
</style>
</head>
<body>
<div class="flyer">
  <div class="side-panel"></div>
  <svg class="panel-notch" width="50" height="66" viewBox="0 0 50 66"><polygon points="0,0 49,33 0,66" fill="var(--blue-mid)"/></svg>

  <svg class="calendar-badge" width="72" height="72" viewBox="0 0 72 72" aria-hidden="true">
    <circle cx="36" cy="36" r="34.5" fill="none" stroke="var(--white)" stroke-width="2.5"/>
    <rect x="19" y="22" width="34" height="30" rx="4" fill="none" stroke="var(--white)" stroke-width="2.5"/>
    <line x1="27" y1="18" x2="27" y2="25" stroke="var(--white)" stroke-width="2.5" stroke-linecap="round"/>
    <line x1="45" y1="18" x2="45" y2="25" stroke="var(--white)" stroke-width="2.5" stroke-linecap="round"/>
    <g fill="var(--white)">
      <circle cx="27" cy="33" r="2"/><circle cx="33" cy="33" r="2"/><circle cx="39" cy="33" r="2"/><circle cx="45" cy="33" r="2"/>
      <circle cx="27" cy="42" r="2"/><circle cx="33" cy="42" r="2"/><circle cx="39" cy="42" r="2"/><circle cx="45" cy="42" r="2"/>
    </g>
  </svg>

  <h1 class="title">
    <div class="title-year">2018</div>
    <div class="title-kicker">CALENDAR</div>
    <div class="title-main">LUNCH</div>
    <div class="title-sub"><span class="title-amp">&amp;</span> <span class="title-accent">LEARN</span></div>
  </h1>
  <div class="title-rule"></div>

  <svg class="meal-icons" width="100" height="206" viewBox="0 0 100 206" aria-hidden="true">
    <g fill="var(--white)">
      <rect x="1" y="2" width="5" height="40" rx="2"/>
      <rect x="11" y="2" width="5" height="40" rx="2"/>
      <rect x="21" y="2" width="5" height="40" rx="2"/>
      <rect x="31" y="2" width="5" height="40" rx="2"/>
      <path d="M1 38 H36 Q36 66 22 76 L26 196 Q26 204 18.5 204 Q11 204 11 196 L15 76 Q1 66 1 38 Z"/>
    </g>
    <g fill="none" stroke="var(--white)" stroke-width="4" stroke-linejoin="round">
      <rect x="65" y="2" width="14" height="16" rx="2"/>
      <path d="M62 18 H82 V168 L76 196 Q72 204 68 196 L62 168 Z"/>
      <line x1="62" y1="160" x2="82" y2="160"/>
      <path d="M82 34 Q94 34 94 46 V104"/>
    </g>
  </svg>

  <div class="site-url">www.veridia.com</div>

  <div class="brand"><span class="brand-dot"></span><span class="brand-name">veridia</span></div>

  <div class="schedule">
    <div class="schedule-row" style="height:38px"><div class="schedule-month">MARCH</div><div class="schedule-topic">Mindfulness</div></div>
    <div class="schedule-row" style="height:72px"><div class="schedule-month">APRIL</div><div class="schedule-topic">Nutrition and Lifestyle<br>Coaching</div></div>
    <div class="schedule-row" style="height:72px"><div class="schedule-month">MAY</div><div class="schedule-topic">What is<br>Neuromodulation?</div></div>
    <div class="schedule-row" style="height:48px"><div class="schedule-month">JUNE</div><div class="schedule-topic">Achieve Your Goals</div></div>
    <div class="schedule-row" style="height:70px"><div class="schedule-month">JULY</div><div class="schedule-topic">Changing Your Life with<br>Positive Thinking</div></div>
    <div class="schedule-row" style="height:97px"><div class="schedule-month">AUG</div><div class="schedule-topic">What is Clean Eating<br>and How Do I Get<br>Started</div></div>
    <div class="schedule-row" style="height:72px"><div class="schedule-month">SEPT</div><div class="schedule-topic">Budgeting 101 Financial<br>Wellness</div></div>
    <div class="schedule-row" style="height:71px"><div class="schedule-month">OCT</div><div class="schedule-topic">Busted I Nutrition<br>Myths</div></div>
    <div class="schedule-row" style="height:72px"><div class="schedule-month">NOV</div><div class="schedule-topic">Time Management: No<br>time like the present</div></div>
    <div class="schedule-row" style="height:41px"><div class="schedule-month">DEC</div><div class="schedule-topic">1st Time Home Buyers</div></div>
  </div>

  <div class="motto">LIFE.<br>LONG.<br>LEARN.</div>
</div>
</body>
</html>
```